Brontal Land Associates Web Site

We need a website design for a new land purchasing and development business based in PEI. We are just regular guys trying a new adventure buying small parcels of land, doing the hard work seperating them into lots, building roads and selling off a dream location. We help folks like ourselves buy the lots, create a house plan and help get the project done.

We have a wordpress website, but no skills. The site should have our simple story and links to individual land development progects, currently we have 2. The larger project is on a golf course and images have been uploaded. We would like a map of the properities with locations on the properties you can click to see the views/ pictures. It would be great to have the ability to superimpose house images on the lot images. This would help prospects see the end results. I have attached some photos and logo's, however, they are not manditory.
The project would have to allow for us to update and maintain the site.

Target Market(s)

Visitors to PEI, typically from larger cities in Ontario and Maine. Golfers that want to live on a golf course.

Industry/Entity Type

Realestate (land development)

Coding

Coded - Design and coding required

Number of Pages Required

4 page

Requirements
Must have
• Allow fo us to maintain the site. Company overview page with story and contact information. Links to current realestate projects (developments). Project pages with the informaiton on the land and purchasing. Since this is land not houses, maps to the site, maps of the parcel, maps of the individual lots with the ability to review photos based on the views of that particular lot.
Nice to have
• The ability to upload and overlay a house picture on the lot. This would provide a visual of the final build.

```html
<!DOCTYPE html>
<html lang="en">
<head>
<meta charset="utf-8">
<title>Brontal Land Associates</title>
<link rel="stylesheet" href="https://fonts.googleapis.com/css2?family=Montserrat:ital,wght@0,500;0,600;0,700;0,800;1,800;1,900&family=Roboto:wght@400;500&display=swap">
<style>
:root{
  --navy:#0b2f5e;
  --navy-deep:#06224a;
  --sky:#3cb4e2;
  --sky-soft:#47bbe4;
  --ink:#333;
  --muted:#8a8a8a;
  --footer:#1e1e21;
  --white:#fff;
}
*{margin:0;padding:0;box-sizing:border-box}
html,body{width:1200px;height:3065px;overflow:hidden}
body{position:relative;background:var(--white);font-family:'Roboto',sans-serif;color:var(--ink)}
.abs{position:absolute}
.topline{left:0;top:0;width:1200px;height:6px;background:var(--navy-deep)}
.header{left:0;top:6px;width:1200px;height:111px;background:var(--white)}
.brand{display:flex;align-items:center;gap:12px;font-family:'Montserrat',sans-serif;font-weight:700}
.brand-mark{width:66px;height:66px;border-radius:50%;background:var(--navy);flex:none}
.brand-name{font-size:22px;line-height:1.1;color:var(--navy);width:210px}
.header .brand{left:113px;top:22px}
.nav{left:476px;top:43px;display:flex;font-size:16px;color:#333}
.nav a{color:inherit;text-decoration:none;position:absolute;white-space:nowrap}
.btn{display:flex;align-items:center;justify-content:center;font-family:'Montserrat',sans-serif;font-weight:700;color:var(--white);border-radius:30px;text-transform:uppercase}
.btn-login{left:954px;top:32px;width:134px;height:55px;background:var(--sky);font-size:16px}
.btn-dark{background:linear-gradient(#1f73b8,var(--navy-deep))}
.hero{left:0;top:117px;width:1200px;height:680px;background:linear-gradient(180deg,#a9c6d7 0%,#d9c7b3 24%,#5d6b3e 34%,#7e7a45 52%,#b3873e 62%,#4d5a2b 80%,#3c3c34 100%)}
.hero-title{left:0;top:205px;width:1200px;text-align:center;font-family:'Montserrat',sans-serif;font-weight:900;font-style:italic;font-size:68px;color:var(--navy)}
.hero-title span{color:var(--sky)}
.btn-start{left:516px;top:333px;width:169px;height:48px;font-size:17px}
.wave{left:0;top:117px}
.about-visual{left:144px;top:805px;width:406px;height:406px;border-radius:50%;background:linear-gradient(180deg,#cde4ef 0%,#d9c8b1 30%,#6e7643 55%,#4d4a2e 100%)}
.section-title{font-family:'Montserrat',sans-serif;font-weight:600;font-size:37px;color:var(--navy)}
.section-title span{color:var(--sky)}
.rule{height:4px;background:var(--sky);width:40px}
.about-title{left:600px;top:835px}
.about-rule{left:600px;top:882px;width:72px}
.about-text{left:600px;top:912px;width:488px;font-size:16px;line-height:30px;color:#333}
.btn-learn{left:600px;top:1121px;width:153px;height:51px;font-size:15px}
.projects{left:0;top:1297px;width:1200px;height:600px;background:linear-gradient(180deg,var(--sky-soft) 0%,var(--sky-soft) 30%,#3da8d4 100%)}
.projects-title{left:0;top:1362px;width:1200px;text-align:center;color:var(--white)}
.projects-rule{left:581px;top:1413px;background:var(--white)}
.card{overflow:hidden}
.card-label{position:absolute;left:0;right:0;bottom:22px;text-align:center;font-family:'Montserrat',sans-serif;font-weight:600;font-size:20px;color:var(--white)}
.card-shade{position:absolute;left:0;right:0;bottom:0;height:45%;background:linear-gradient(rgba(6,34,74,0),rgba(6,40,80,.9))}
.contact-map{left:111px;top:2175px;width:364px;height:364px;border-radius:50%;background:radial-gradient(circle,#fbfbfb 0%,#eeeeee 80%,#e2e2e2 100%);box-shadow:0 4px 14px rgba(0,0,0,.12)}
.contact-title{left:548px;top:2150px;width:540px;text-align:center}
.contact-rule{left:798px;top:2197px}
.field{background:var(--white);border-radius:6px;box-shadow:0 2px 12px rgba(0,0,0,.1);font-size:14px;color:#666;padding:0 22px;display:flex;align-items:center}
.field-msg{align-items:center}
.btn-submit{left:753px;top:2514px;width:128px;height:52px;font-size:16px}
.footer{left:0;top:2667px;width:1200px;height:398px;background:var(--footer);color:var(--white)}
.footer .brand-name{color:var(--white)}
.footer .brand-mark{background:var(--white)}
.partner{left:115px;top:2864px;display:flex;align-items:center;gap:14px;font-family:'Montserrat',sans-serif;font-weight:600;font-size:22px;color:var(--white)}
.partner-mark{width:50px;height:50px;border-radius:50%;background:#8cbf7a}
.vline{left:390px;top:2736px;width:1px;height:208px;background:#3a3a3e}
.fcol h4{font-family:'Montserrat',sans-serif;font-weight:700;font-size:20px;margin-bottom:14px}
.fcol ul{list-style:none;font-size:15px;line-height:25.6px}
.fcol li::before{content:"»";margin-right:12px}
.contact-list{font-size:15px}
.contact-list div{display:flex;gap:10px;align-items:flex-start;margin-bottom:16px;line-height:25px}
.contact-list svg{flex:none;margin-top:5px}
.hline{left:112px;top:2974px;width:976px;height:1px;background:#3a3a3e}
.copy{left:113px;top:3008px;font-size:15px}
.social{width:38px;height:38px;border-radius:50%;top:2998px}
</style>
</head>
<body>
<div class="abs topline"></div>

<header class="abs header">
  <div class="abs brand"><span class="brand-mark"></span><span class="brand-name">Brontal Land Associates</span></div>
  <nav class="abs nav">
    <a style="left:0">Home</a>
    <a style="left:84px">About</a>
    <a style="left:166px">Services</a>
    <a style="left:266px">Project</a>
    <a style="left:357px">Contact Us</a>
  </nav>
  <div class="abs btn btn-login">Log In</div>
</header>

<section class="abs hero" role="img" aria-label="Photo of a rural road beside wildflower meadows and rolling wooded hills at sunset"></section>
<h1 class="abs hero-title">Welcome <span>To Brontal</span></h1>
<div class="abs btn btn-dark btn-start">Get Started</div>

<svg class="abs wave" width="1200" height="680" viewBox="0 0 1200 680" aria-hidden="true">
  <path d="M0,561 C150,530 260,505 400,528 C520,548 580,585 720,616 C900,656 1100,664 1200,612 L1200,680 L0,680 Z" fill="#fff"/>
  <path d="M0,567 C150,536 260,511 400,534 C520,554 580,591 720,622 C900,662 1100,670 1200,618" fill="none" stroke="#0b2f5e" stroke-width="8"/>
  <path d="M0,561 C150,530 260,505 400,528 C520,548 580,585 720,616 C900,656 1100,664 1200,612" fill="none" stroke="#3cb4e2" stroke-width="5"/>
  <circle cx="600" cy="578" r="31" fill="#fff"/>
  <circle cx="600" cy="578" r="25" fill="#3cb4e2"/>
  <rect x="593" y="563" width="14" height="20" rx="7" fill="none" stroke="#fff" stroke-width="2"/>
  <line x1="600" y1="567" x2="600" y2="572" stroke="#fff" stroke-width="2"/>
  <path d="M600,586 V594 M596,590 L600,594 L604,590" fill="none" stroke="#fff" stroke-width="2"/>
</svg>

<div class="abs about-visual" role="img" aria-label="Circular photo of meadow grass and evergreen trees"></div>
<h2 class="abs section-title about-title">About <span>us</span></h2>
<div class="abs rule about-rule"></div>
<p class="abs about-text">Lorem ipsum dolor sit amet, consectetur adipiscing elit, sed do eiusmod tempor incididunt ut labore et dolore magna aliqua.Ut enim ad minim veniam, quis nostrud exercitation ullamco laboris nisi ut aliquip ex ea commodo consequat. Duis aute irure dolor in reprehenderit in voluptate velit esse cillum dolore eu fugiat nulla pariatur. Excepteur sint occaecat cupidatat non proident, sunt in culpa qui officia deserunt mollit anim id</p>
<div class="abs btn btn-dark btn-learn">Learn More</div>

<section class="abs projects"></section>
<h2 class="abs section-title projects-title">Our Projects</h2>
<div class="abs rule projects-rule"></div>

<div class="abs card" style="left:112px;top:1467px;width:476px;height:326px;background:linear-gradient(180deg,#b7d3ec 0%,#d8e6f1 25%,#2f5e2c 45%,#3f8a3a 70%,#2d6b33 100%)" role="img" aria-label="Photo of a golf course fairway lined with tall trees"><div class="card-shade"></div><div class="card-label">Golf Course</div></div>
<div class="abs card" style="left:613px;top:1467px;width:475px;height:326px;background:linear-gradient(180deg,#9fb4c2 0%,#d7c8ae 40%,#3e452d 58%,#55573a 78%,#2c2e24 100%)" role="img" aria-label="Photo of a gravel road through a grassy field at dusk"><div class="card-shade"></div><div class="card-label">Individual Land Development</div></div>
<div class="abs card" style="left:112px;top:1820px;width:307px;height:252px;background:linear-gradient(180deg,#a8b6c6 0%,#d5b9a4 32%,#3d4128 48%,#6a6140 75%,#3a3526 100%)" role="img" aria-label="Photo of a tall grass field with distant trees"><div class="card-shade"></div><div class="card-label">Lorem ipsum</div></div>
<div class="abs card" style="left:447px;top:1820px;width:307px;height:252px;background:linear-gradient(180deg,#4a62d8 0%,#8c9ce8 25%,#3f7a34 45%,#5ea642 70%,#3a7d33 100%)" role="img" aria-label="Photo of a resort clubhouse beside a green golf course"><div class="card-shade"></div><div class="card-label">Lorem ipsum</div></div>
<div class="abs card" style="left:781px;top:1820px;width:307px;height:252px;background:linear-gradient(180deg,#a5bfd2 0%,#d8c3a8 30%,#545a36 45%,#8b7b4c 70%,#3d3c30 100%)" role="img" aria-label="Photo of wildflower meadow and country road at sunset"><div class="card-shade"></div><div class="card-label">Lorem ipsum</div></div>

<div class="abs contact-map" role="img" aria-label="Circular site plan map of the lots with numbered markers and house locations"></div>
<h2 class="abs section-title contact-title">Contact <span>Us</span></h2>
<div class="abs rule contact-rule"></div>
<div class="abs field" style="left:548px;top:2247px;width:257px;height:63px">First Name</div>
<div class="abs field" style="left:831px;top:2247px;width:257px;height:63px">Last Name</div>
<div class="abs field" style="left:548px;top:2334px;width:257px;height:63px">Phone</div>
<div class="abs field" style="left:831px;top:2334px;width:257px;height:63px">Email</div>
<div class="abs field field-msg" style="left:548px;top:2420px;width:537px;height:63px">Message</div>
<div class="abs btn btn-dark btn-submit">Submit</div>

<footer class="abs footer"></footer>
<div class="abs brand" style="left:115px;top:2770px"><span class="brand-mark"></span><span class="brand-name">Brontal Land Associates</span></div>
<div class="abs partner"><span class="partner-mark"></span><span>Crestmoor Links</span></div>
<div class="abs vline"></div>

<div class="abs fcol" style="left:432px;top:2730px;color:#fff">
  <h4>Quick Links</h4>
  <ul><li>Home</li><li>About</li><li>Services</li><li>Project</li><li>Contact Us</li></ul>
</div>
<div class="abs fcol" style="left:640px;top:2730px;color:#fff">
  <h4>Our Company</h4>
  <ul><li>Terms &amp; Conditions</li><li>Privacy Policy</li><li>About Us</li><li>Support</li></ul>
</div>
<div class="abs fcol" style="left:864px;top:2730px;width:230px;color:#fff">
  <h4>Contact us</h4>
  <div class="contact-list">
    <div><svg width="13" height="17" viewBox="0 0 13 17"><path d="M6.5,0 C10,0 13,2.8 13,6.3 C13,10.5 6.5,17 6.5,17 C6.5,17 0,10.5 0,6.3 C0,2.8 3,0 6.5,0 Z" fill="#fff"/><circle cx="6.5" cy="6.3" r="2.4" fill="#1e1e21"/></svg><span>Lorem ipsum dolor sit amet, consectetur adipiscing</span></div>
    <div><svg width="17" height="17" viewBox="0 0 17 17"><path d="M3.5,0.5 L6.5,4.5 L4.8,6.6 C5.8,8.8 8.2,11.2 10.4,12.2 L12.5,10.5 L16.5,13.5 L14.5,16.5 C7,16 1,10 0.5,2.5 Z" fill="#fff"/></svg><span>1+ (555) 010 2040</span></div>
    <div><svg width="17" height="13" viewBox="0 0 17 13"><rect width="17" height="13" rx="1.5" fill="#fff"/><path d="M1,1.5 L8.5,7.5 L16,1.5" fill="none" stroke="#1e1e21" stroke-width="1.5"/></svg><span>info@brontalland.com</span></div>
  </div>
</div>

<div class="abs hline"></div>
<div class="abs copy" style="color:#fff">©Copyrights 2022 Brontal Land Associates &nbsp;&nbsp;| &nbsp;&nbsp;All Rights Reserved</div>
<div class="abs social" style="left:920px;background:#1f73b8"></div>
<div class="abs social" style="left:962px;background:#fff"></div>
<div class="abs social" style="left:1005px;background:#fff"></div>
<div class="abs social" style="left:1048px;background:#fff"></div>
</body>
</html>
```